Podiatry clinic requires a modern revamp and editing of existing website.

I would like a fresh new look and updated information for my current business website. An easy to navigate site with prominent address and phone number for call to action. We are a podiatry clinic that focuses on general and sports podiatry.
I would like 4 pages; including Home page, About Us, Services & Contact.
www.brambleridgefootcare.com

Target Market(s)

Active working professionals.

Industry/Entity Type

Medical

Coding

Coded - Design and coding required

Number of Pages Required

4 page

Font styles to use
Sans Serif

Colors
6b449b

Requirements
Must have
• A modern look with logo and active images; clean and uncluttered. Visible phone number and address for call to action.
• 4 pages - Home, About Us, Services, Contact.
• Home page - update address & service logos.
• About Us - update of personal information.
• Services - Revamp of existing page.
• Contact page to include Google map, email & phone number.
Nice to have
• Ability to add content easily; eg. a blog or adding video onto Home page.
• Link to Facebook page.

```html
<!DOCTYPE html>
<html lang="en">
<head>
<meta charset="utf-8">
<title>Bramble Ridge Foot Care</title>
<link href="https://fonts.googleapis.com/css2?family=Open+Sans:wght@300;400;600;700&display=swap" rel="stylesheet">
<style>
  :root {
    --lavender: #9b86c0;
    --purple: #6b449b;
    --page: #f4f6f9;
    --ink: #2f2f2f;
    --text: #1e1e1e;
    --white: #ffffff;
    --badge: #dcdfe6;
  }
  * { margin: 0; padding: 0; box-sizing: border-box; }
  html, body { width: 1107px; height: 1200px; overflow: hidden; }
  body { font-family: "Open Sans", sans-serif; background: var(--page); position: relative; }

  .site-header { position: absolute; left: 0; top: 0; width: 1107px; height: 173px; background: var(--lavender); color: var(--white); }
  .header-address { position: absolute; left: 43px; top: 60px; display: flex; gap: 14px; font-size: 15.5px; line-height: 21px; }
  .header-address svg { margin-top: 2px; }
  .brand { position: absolute; left: 466px; top: 56px; width: 240px; display: flex; align-items: center; gap: 12px; }
  .brand-mark { width: 40px; height: 40px; border-radius: 50%; background: var(--purple); flex: none; }
  .brand-name { font-size: 22px; font-weight: 600; line-height: 28px; color: var(--white); white-space: nowrap; }
  .header-phone { position: absolute; left: 866px; top: 66px; display: flex; align-items: center; gap: 14px; font-size: 26px; font-weight: 400; }

  .main-nav { position: absolute; left: 0; top: 173px; width: 1107px; height: 53px; background: var(--purple); }
  .main-nav a { position: absolute; top: 16px; color: var(--white); text-decoration: none; font-size: 15.5px; transform: translateX(-50%); }
  .nav-divider { position: absolute; top: 19px; width: 1px; height: 16px; background: rgba(255,255,255,0.55); }

  .hero { position: absolute; left: 0; top: 226px; width: 1107px; height: 424px; overflow: hidden; }
  .hero-image { position: absolute; inset: 0;
    background:
      linear-gradient(rgba(20,18,22,0.35), rgba(20,18,22,0.35)),
      radial-gradient(ellipse at 50% 75%, #8a7f78 0%, #5d544f 35%, transparent 70%),
      linear-gradient(90deg, #4b4a52 0%, #7a7173 30%, #8f7a5a 55%, #9a7a45 75%, #4a3c34 100%); }
  .hero-title { position: absolute; left: 0; top: 78px; width: 100%; text-align: center; color: var(--white); font-weight: 300; font-size: 46px; line-height: 60px; }
  .hero-subtitle { position: absolute; left: 0; width: 100%; top: 163px; text-align: center; color: var(--white); font-weight: 700; font-size: 26px; }
  .hero-button { position: absolute; left: 398px; top: 246px; width: 302px; height: 50px; border: 1px solid var(--white); color: var(--white); font-size: 17px; font-weight: 300; display: flex; align-items: center; justify-content: center; text-decoration: none; }

  .section-title { position: absolute; top: 706px; font-size: 29px; font-weight: 700; color: var(--ink); }
  .about-title { left: 41px; }
  .services-title { left: 574px; }
  .about-text { position: absolute; left: 43px; top: 785px; width: 475px; font-size: 15.5px; line-height: 22.5px; color: var(--text); }
  .about-text p + p { margin-top: 22.5px; }

  .partner-badge { position: absolute; background: var(--badge); border-radius: 6px; }

  .site-footer { position: absolute; left: 0; top: 1159px; width: 1107px; height: 41px; background: var(--purple); color: var(--white); font-size: 12.5px; font-weight: 700; display: flex; align-items: center; justify-content: center; }
</style>
</head>
<body>
  <header class="site-header">
    <div class="header-address">
      <svg width="16" height="24" viewBox="0 0 16 24" aria-hidden="true"><path d="M8 0C3.6 0 0 3.5 0 7.9 0 13.5 8 24 8 24s8-10.5 8-16.1C16 3.5 12.4 0 8 0zm0 11a3.1 3.1 0 1 1 0-6.2A3.1 3.1 0 0 1 8 11z" fill="#fff"/></svg>
      <span>Suite 208 / 155 Larchmont<br>Street Melbourne 3000</span>
    </div>
    <div class="brand">
      <span class="brand-mark"></span>
      <span class="brand-name">Bramble Ridge<br>Foot Care</span>
    </div>
    <div class="header-phone">
      <svg width="14" height="22" viewBox="0 0 14 22" aria-hidden="true"><rect x="1.5" y="1.5" width="11" height="19" rx="2" fill="none" stroke="#fff" stroke-width="2.4"/><rect x="5" y="16" width="4" height="2" fill="#fff"/></svg>
      <span>1300 552 784</span>
    </div>
  </header>

  <nav class="main-nav">
    <a href="#" style="left:356px">Home</a>
    <span class="nav-divider" style="left:418px"></span>
    <a href="#" style="left:490px">About us</a>
    <span class="nav-divider" style="left:568px"></span>
    <a href="#" style="left:643px">Services</a>
    <span class="nav-divider" style="left:706px"></span>
    <a href="#" style="left:777px">Contact us</a>
  </nav>

  <section class="hero">
    <div class="hero-image" role="img" aria-label="Photo of the clinic reception desk and waiting area"></div>
    <h1 class="hero-title">Lorem ipsum dolor sit amet</h1>
    <p class="hero-subtitle">ONSECTETUR ADIPISCING ELIT.</p>
    <a class="hero-button" href="#">TEXT GOES HERE</a>
  </section>

  <h2 class="section-title about-title">Some words about us</h2>
  <div class="about-text">
    <p>Bramble Ridge Foot Care is a Podiatry clinic in the heart of Melbourne CBD. We are located between Reed &amp; Alder Streets in the Alder Park Business Centre / Reed Hotel Complex.</p>
    <p>Our podiatrists are fully qualified health professionals who are able to diagnose, treat, manage or help to prevent all medical conditions that affect the feet and lower limb.</p>
    <p>We provide General Podiatry Treatment and some Specialised Services in relation to various foot conditions, including Sports Injuries, Orthotic Therapy and Nail Surgery.</p>
    <p>For Appointments or Enquiries please call us on 1300 552 784 or email:&nbsp;&nbsp; info@brambleridgefootcare.com</p>
  </div>

  <h2 class="section-title services-title">Our Services</h2>
  <div class="partner-badge" style="left:574px;top:780px;width:211px;height:64px" role="img" aria-label="Health claims partner badge"></div>
  <div class="partner-badge" style="left:865px;top:780px;width:114px;height:48px" role="img" aria-label="Sports podiatry association badge"></div>
  <div class="partner-badge" style="left:573px;top:898px;width:205px;height:54px" role="img" aria-label="Public health insurer badge"></div>
  <div class="partner-badge" style="left:853px;top:902px;width:126px;height:54px" role="img" aria-label="Sports medicine body badge"></div>

  <footer class="site-footer">Copyright © 2012 - 2016 Bramble Ridge Foot Care. All rights reserved.</footer>
</body>
</html>
```